Design Build and Remodeling Contractors....needs Flyer Design

We need flyer design for residential construction services. We would like the design to be appealing and stand out amongst a hand full of other mailers. Colors we would like to implement are navy blue and fluorescent/highlighter yellow. We have uploaded our company logo and phone number.

Industry/Entity Type

Residential

```html
<!DOCTYPE html>
<html lang="en">
<head>
<meta charset="utf-8">
<title>Summit Build Services – Flyer</title>
<link rel="stylesheet" href="https://fonts.googleapis.com/css2?family=Signika:wght@400;600;700&family=PT+Sans+Narrow:wght@400;700&family=Lato:wght@700&display=swap">
<style>
  :root {
    --navy: #0b1240;
    --navy-deep: #060a2a;
    --royal: #1c2f8f;
    --sky-blue: #1f7fd0;
    --logo-blue: #1565b8;
    --highlight: #fff200;
    --amber: #ffc60b;
    --white: #ffffff;
    --page-bg: #e4e4e4;
    --text-dark: #14185a;
  }
  * { box-sizing: border-box; margin: 0; padding: 0; }
  html, body { width: 1200px; height: 857px; overflow: hidden; }
  body { background: var(--page-bg); font-family: "Signika", sans-serif; }

  .flyer {
    position: absolute; left: 312px; top: 24px;
    width: 576px; height: 808px;
    background: var(--white); overflow: hidden;
    box-shadow: 0 2px 8px rgba(0,0,0,.15);
  }

  .photo-house {
    position: absolute; left: 0; top: 0; width: 576px; height: 340px;
    background: linear-gradient(180deg, #dfe7ee 0%, #cfd8e0 25%, #3b3f4a 38%, #3b3f4a 48%, #8a5a48 52%, #7a4c3c 78%, #6f8d4b 88%, #5f7c3c 100%);
  }
  .photo-site {
    position: absolute; left: 0; top: 330px; width: 330px; height: 400px;
    background: linear-gradient(90deg, #c9ccd2 0%, #dfe2e6 55%, rgba(255,255,255,0) 100%);
  }
  .photo-team {
    position: absolute; left: 0; top: 470px; width: 300px; height: 255px;
    background: linear-gradient(160deg, #e6a43a 0%, #9aa0a8 35%, #5b5f66 70%, #3e4147 100%);
    border-top-right-radius: 40px;
    opacity: .9;
  }

  .swoosh { position: absolute; left: 0; top: 0; width: 576px; height: 460px; }

  .brand {
    position: absolute; left: 24px; top: 0; width: 160px; height: 118px;
    background: linear-gradient(180deg, #2b8fe0 0%, var(--logo-blue) 55%, var(--navy) 100%);
    border-radius: 0 0 10px 10px;
    display: flex; align-items: flex-end; justify-content: center; padding-bottom: 18px;
  }
  .brand-name {
    font-family: "Signika", sans-serif; font-weight: 600; color: var(--highlight);
    font-size: 19px; line-height: 1.05; text-align: center;
  }

  .headline {
    position: absolute; left: 268px; top: 10px; width: 308px; height: 52px;
    background: linear-gradient(90deg, rgba(255,242,0,0) 0%, var(--highlight) 22%);
    text-align: right; padding-right: 24px; color: var(--navy);
  }
  .headline-title { font-weight: 700; font-size: 21px; line-height: 26px; padding-top: 2px; }
  .headline-sub { font-family: "PT Sans Narrow", sans-serif; font-weight: 700; font-size: 16px; line-height: 18px; }

  .services-title {
    position: absolute; left: 300px; top: 410px;
    font-family: "PT Sans Narrow", sans-serif; font-weight: 700;
    font-size: 17px; color: var(--text-dark); letter-spacing: .2px;
  }
  .sectors { position: absolute; left: 318px; top: 443px; display: flex; gap: 18px; }
  .sector { width: 58px; text-align: center; }
  .sector-icon {
    width: 58px; height: 52px; background: var(--royal);
    display: flex; align-items: center; justify-content: center;
  }
  .sector-label {
    font-family: "PT Sans Narrow", sans-serif; font-weight: 700; font-size: 12px;
    color: var(--navy); margin-top: 4px; margin-left: -10px; margin-right: -10px;
  }

  .service-list {
    position: absolute; top: 531px; list-style: none;
    font-family: "PT Sans Narrow", sans-serif; font-size: 12.5px; color: var(--text-dark);
  }
  .service-list li { height: 13.8px; line-height: 13.8px; padding-left: 8px; position: relative; }
  .service-list li::before {
    content: ""; position: absolute; left: 0; top: 3.5px;
    border-left: 5px solid var(--royal); border-top: 3.5px solid transparent; border-bottom: 3.5px solid transparent;
  }
  .list-a { left: 299px; }
  .list-b { left: 433px; }

  .footer {
    position: absolute; left: 0; bottom: 0; width: 576px; height: 84px;
    background: linear-gradient(180deg, var(--sky-blue) 0%, var(--royal) 14%, var(--navy-deep) 34%, var(--navy) 100%);
    padding: 13px 0 0 45px;
    font-family: "Lato", sans-serif; font-weight: 700; font-variant: small-caps;
    color: var(--white); font-size: 11px; letter-spacing: 1.4px; line-height: 13.6px;
  }
</style>
</head>
<body>
<main class="flyer">
  <div class="photo-house" role="img" aria-label="Photo of a brick single-storey house with a dark tiled roof and garage"></div>
  <div class="photo-site" role="img" aria-label="Photo of a high-rise apartment building under construction"></div>
  <div class="photo-team" role="img" aria-label="Photo of a contractor in hard hat and a client reviewing building plans"></div>

  <svg class="swoosh" viewBox="0 0 576 460" aria-hidden="true">
    <path d="M0 300 C150 330 360 290 576 90 L576 250 C430 420 200 440 0 330 Z" fill="#ffffff"/>
    <path d="M0 282 C160 330 380 300 576 95 L576 130 C400 330 170 360 0 305 Z" fill="#1f6fc8"/>
    <path d="M0 296 C170 345 400 310 576 130 L576 175 C410 350 190 370 0 315 Z" fill="#0f2f8f"/>
    <path d="M0 300 C140 360 340 350 576 250 L576 270 C360 380 150 395 0 330 Z" fill="#ffc60b"/>
    <path d="M0 330 C160 400 360 395 576 280 L576 300 C380 410 170 420 0 345 Z" fill="#fff200" opacity=".85"/>
  </svg>

  <div class="brand"><span class="brand-name">SUMMIT BUILD<br>SERVICES INC</span></div>

  <header class="headline">
    <div class="headline-title">We Create Dream Homes!</div>
    <div class="headline-sub">RESIDENTIAL &amp; COMMERCIAL CONTRACTORS</div>
  </header>

  <h2 class="services-title">GENERAL CONTRACTOR SPECIALIZING IN</h2>

  <div class="sectors">
    <div class="sector">
      <div class="sector-icon">
        <svg width="42" height="36" viewBox="0 0 42 36" fill="#fff"><rect x="2" y="18" width="10" height="16"/><rect x="14" y="6" width="10" height="28"/><rect x="26" y="12" width="12" height="22"/><rect x="0" y="34" width="42" height="2"/></svg>
      </div>
      <div class="sector-label">COMMERCIAL</div>
    </div>
    <div class="sector">
      <div class="sector-icon">
        <svg width="42" height="36" viewBox="0 0 42 36" fill="#fff"><rect x="4" y="4" width="4" height="16"/><rect x="11" y="8" width="4" height="12"/><path d="M2 20 L14 14 L14 20 L26 14 L26 20 L40 14 L40 34 L2 34 Z"/></svg>
      </div>
      <div class="sector-label">INDUSTRIAL</div>
    </div>
    <div class="sector">
      <div class="sector-icon">
        <svg width="42" height="36" viewBox="0 0 42 36" fill="#fff"><path d="M21 2 L40 16 L36 16 L36 34 L6 34 L6 16 L2 16 Z"/><rect x="17" y="22" width="8" height="12" fill="#1c2f8f"/></svg>
      </div>
      <div class="sector-label">RESIDENTIAL</div>
    </div>
  </div>

  <ul class="service-list list-a">
    <li>New Construction</li><li>Renovations</li><li>Building Altertinos</li><li>Building Expansions</li>
    <li>Retail</li><li>Institutional</li><li>Hotels</li><li>Casinos</li><li>Restaurants</li>
    <li>Malls</li><li>Offices</li><li>Auto Facilities</li><li>Parking Structures, Etc.</li>
  </ul>
  <ul class="service-list list-b">
    <li>Custom Concrete</li><li>Stamped &amp; Decorative</li><li>Waterproofing &amp; Sealing</li><li>Framing</li>
    <li>Drywall</li><li>Electrcal</li><li>Plumbing</li><li>FLooring</li><li>Painting</li>
    <li>Roofing</li><li>Ground upto Completion</li><li>Design/Build</li><li>Maintenance</li>
  </ul>

  <footer class="footer">
    <div>We Create Dream Homes! Residential &amp; Commercial Contractors.</div>
    <div>Call Now. 800-555-0142</div>
    <div>P.O.Box: 412, Maple Ridge, CA 90000</div>
    <div>sales@summitbuild.example</div>
    <div>LIC# 000000</div>
  </footer>
</main>
</body>
</html>
```